Billboard for Law Firm

I am looking for a billboard designs. Our branding right now is not good. The logo has to stay the same, but please help come up with something modern, airy, perhaps geometric for the supporting design elements.
Colors should probably be red and blue, or shades of blue, but you can play with the exact shades. Doesn't have to match what you see in the attachment.

The billboard should include:

- Some type of design to bring it to life.

- Logo

- Accident & Injury Law

- 614.300.7000

- Disclaimer (very small text): No Representation Made That The Quality of Legal Services Performed is Greater Than the Those of Other Attorneys

Slogan (very large): Grits, Gravy, and a Good Attorney

______________

Target Market(s)

Southern United States

Industry/Entity Type

Legal Services

Font styles to use
Serif
Sans Serif

Colors
0054AA
0677BA
7BADD7
CADEEF
E8F1F8
EB3D1F
EC4F4E
F09395
F8D3D4
FCEDEE

Requirements
Must have
• Help Make it Memorable and Easy to Read (large text for slogan)
Nice to have
• Some shapes or design elements that may become part of our branding.

```html
<!DOCTYPE html>
<html lang="en">
<head>
<meta charset="UTF-8">
<title>The Harlow Firm – Billboard</title>
<link href="https://fonts.googleapis.com/css2?family=Montserrat:wght@400;500;700;800;900&display=swap" rel="stylesheet">
<style>
  :root{
    --navy:#0b0f5c;
    --red:#d3292a;
    --ink:#111111;
    --sky-top:#8cc2ee;
    --sky-mid:#cfe2f2;
    --haze:#eef3f8;
    --city:#6d8aa6;
    --white:#ffffff;
    --page:#ffffff;
  }
  *{margin:0;padding:0;box-sizing:border-box}
  html,body{width:1200px;height:875px;overflow:hidden;background:var(--page)}
  body{position:relative;font-family:"Montserrat",Arial,sans-serif}
  .billboard{
    position:absolute;left:20px;top:115px;width:1160px;height:645px;
    overflow:hidden;background:var(--white);
  }
  .scene{
    position:absolute;inset:0 0 195px 0;
    background:
      linear-gradient(180deg,rgba(255,255,255,0) 70%,rgba(120,145,170,.55) 88%,rgba(90,110,130,.75) 100%),
      linear-gradient(180deg,var(--sky-top) 0%,#b3d4f1 35%,var(--sky-mid) 60%,var(--haze) 80%);
  }
  .ground-fade{
    position:absolute;left:0;right:0;top:440px;bottom:0;
    background:linear-gradient(180deg,#c9d3dc 0%,#f4f6f8 35%,var(--white) 60%);
  }
  .headline{
    position:absolute;left:0;right:0;top:36px;text-align:center;
    font-weight:900;font-size:86px;line-height:86px;letter-spacing:-1px;
  }
  .headline .line-one{color:var(--navy);display:block}
  .headline .line-two{color:var(--red);display:block}
  .disclaimer{
    position:absolute;left:100px;right:100px;top:232px;text-align:center;
    font-size:18.5px;line-height:26px;color:var(--ink);font-weight:400;
  }
  .brand{position:absolute;left:70px;top:490px;width:420px;text-align:center}
  .brand-name{
    display:flex;align-items:center;justify-content:center;gap:12px;
    color:var(--red);font-weight:800;font-size:40px;line-height:1;
  }
  .brand-name .mark{width:22px;height:22px;border-radius:50%;background:var(--red);flex:none}
  .brand-tag{margin-top:14px;color:var(--red);font-size:14px;font-weight:500;letter-spacing:1px;text-transform:uppercase}
  .divider{position:absolute;left:518px;top:495px;width:2px;height:100px;background:var(--navy)}
  .contact{position:absolute;left:565px;top:490px}
  .contact-row{display:flex;align-items:center;gap:22px}
  .contact-row svg{width:34px;height:34px;flex:none}
  .phone{font-weight:900;font-size:60px;line-height:64px;color:var(--ink);letter-spacing:-1px}
  .web{font-weight:500;font-size:44px;line-height:56px;color:var(--ink)}
</style>
</head>
<body>
  <main class="billboard">
    <div class="scene" role="img" aria-label="Photo of a city skyline across calm water under a bright blue sky"></div>
    <div class="ground-fade"></div>

    <h1 class="headline">
      <span class="line-one">GRITS, GRAVY, AND A</span>
      <span class="line-two">GOOD ATTORNEY</span>
    </h1>

    <p class="disclaimer">No Representation Made That The Quality of Legal Services Performed is Greater Than the<br>Those of Other Attorneys</p>

    <div class="brand">
      <div class="brand-name"><span class="mark"></span>The Harlow Firm</div>
      <div class="brand-tag">Injury &amp; Accident Lawyers</div>
    </div>

    <div class="divider"></div>

    <div class="contact">
      <div class="contact-row">
        <svg viewBox="0 0 24 24" aria-hidden="true"><path fill="#d3292a" d="M6.6 10.8a15.5 15.5 0 0 0 6.6 6.6l2.2-2.2c.3-.3.7-.4 1-.2 1.1.4 2.3.6 3.6.6.6 0 1 .4 1 1V20c0 .6-.4 1-1 1A17 17 0 0 1 3 4c0-.6.4-1 1-1h3.5c.6 0 1 .4 1 1 0 1.3.2 2.5.6 3.6.1.3 0 .7-.2 1z"/><path fill="none" stroke="#d3292a" stroke-width="1.8" stroke-linecap="round" d="M14 3.5a7 7 0 0 1 6.5 6.5M14 7a3.5 3.5 0 0 1 3 3"/></svg>
        <span class="phone">614.300.7000</span>
      </div>
      <div class="contact-row">
        <svg viewBox="0 0 24 24" aria-hidden="true"><circle cx="12" cy="12" r="10" fill="#d3292a"/><g fill="none" stroke="#fff" stroke-width="1.4"><ellipse cx="12" cy="12" rx="4" ry="10"/><path d="M2 12h20M4 7h16M4 17h16"/></g></svg>
        <span class="web">harlowinjurylaw.com</span>
      </div>
    </div>
  </main>
</body>
</html>
```